Modern & Innovative business card for new commercial construction company Valdorne - Inc.
Valdorne-Inc
Modern & Innovative business card for new commercial construction company Valdorne - Inc. - Construction
Creative Brief
Professional
Marcus T. Whitfield
President
P.O. Box 3097 Cary, N.C. 27519-3097
MWhitfield@valdorne-inc.example
Either the logo over the entire back of the card with the contact information on the front.

```html
<!DOCTYPE html>
<html lang="en">
<head>
<meta charset="utf-8">
<title>Valdorne - Inc. Business Card</title>
<link href="https://fonts.googleapis.com/css2?family=Montserrat:wght@400;500;600&display=swap" rel="stylesheet">
<style>
  :root {
    --brand-red: #c62f37;
    --brand-red-dark: #a4222a;
    --ink-grey: #6d6e71;
    --light-grey: #c9cacc;
    --paper: #ffffff;
    --backdrop: #ecebe8;
  }
  * { margin: 0; padding: 0; box-sizing: border-box; }
  html, body { width: 1200px; height: 629px; overflow: hidden; }
  body {
    background: var(--backdrop);
    font-family: "Montserrat", sans-serif;
    position: relative;
  }
  .card {
    position: absolute;
    top: 160px;
    width: 530px;
    height: 303px;
    overflow: hidden;
    box-shadow: 0 6px 18px rgba(0,0,0,0.18);
  }
  /* Back side */
  .card-back { left: 45px; background: var(--brand-red); }
  .card-back .back-name {
    position: absolute;
    right: 40px;
    top: 78px;
    color: var(--paper);
    font-size: 34px;
    font-weight: 500;
    letter-spacing: 3px;
    text-transform: uppercase;
  }
  .card-back .back-web {
    position: absolute;
    left: 40px;
    bottom: 34px;
    color: var(--paper);
    font-size: 14px;
    font-weight: 500;
    letter-spacing: 4px;
    text-transform: uppercase;
  }
  /* Front side */
  .card-front { left: 625px; background: var(--paper); }
  .contact-block {
    position: absolute;
    left: 40px;
    top: 34px;
  }
  .holder-name {
    color: var(--brand-red);
    font-size: 15px;
    font-weight: 600;
    letter-spacing: 2px;
    text-transform: uppercase;
  }
  .holder-title {
    color: var(--ink-grey);
    font-size: 11px;
    letter-spacing: 1.5px;
    margin-top: 3px;
    margin-bottom: 12px;
    text-transform: uppercase;
  }
  .contact-line {
    display: flex;
    align-items: center;
    gap: 8px;
    color: var(--ink-grey);
    font-size: 11px;
    line-height: 1.75;
    letter-spacing: 0.5px;
  }
  .contact-icon {
    width: 12px; height: 12px;
    border-radius: 50%;
    background: var(--brand-red);
    flex: none;
  }
  .contact-icon.blank { background: transparent; }
  .brand-mark {
    position: absolute;
    left: 40px;
    bottom: 38px;
    display: flex;
    align-items: center;
    gap: 10px;
  }
  .brand-dot {
    width: 40px; height: 40px;
    border-radius: 50%;
    border: 3px solid var(--brand-red);
  }
  .brand-name {
    color: var(--brand-red);
    font-size: 15px;
    font-weight: 600;
    letter-spacing: 2px;
    text-transform: uppercase;
  }
  .swoosh { position: absolute; right: 0; bottom: 0; }
</style>
</head>
<body>
  <section class="card card-back">
    <div class="back-name">Valdorne</div>
    <div class="back-web">www.valdorne-inc.example</div>
  </section>

  <section class="card card-front">
    <div class="contact-block">
      <div class="holder-name">Marcus T. Whitfield</div>
      <div class="holder-title">President</div>
      <div class="contact-line"><span class="contact-icon"></span>P.O. Box 3097</div>
      <div class="contact-line"><span class="contact-icon blank"></span>Halvern, ST 00519-3097</div>
      <div class="contact-line"><span class="contact-icon"></span>555.010.0142</div>
      <div class="contact-line"><span class="contact-icon"></span>MWhitfield@valdorne-inc.example</div>
      <div class="contact-line"><span class="contact-icon"></span>www.valdorne-inc.example</div>
    </div>

    <div class="brand-mark">
      <span class="brand-dot"></span>
      <span class="brand-name">Valdorne - Inc.</span>
    </div>

    <svg class="swoosh" width="530" height="150" viewBox="0 0 530 150" aria-hidden="true">
      <path d="M170 150 C 300 120, 430 70, 530 10 L 530 150 Z" fill="var(--light-grey)"/>
      <path d="M250 150 C 350 128, 450 90, 530 45 L 530 150 Z" fill="var(--brand-red)"/>
      <path d="M330 150 C 410 135, 480 110, 530 85 L 530 150 Z" fill="var(--brand-red-dark)"/>
    </svg>
  </section>
</body>
</html>
```